Harborline Facility Systems needs a business card design with logo

need a business card and log design for a company called "Harborline Facility Systems". we improve building energy efficiency and save energy costs through building automation systems for commercial buildings such as hospitals, office buildings, universities, etc. The final design should communicate elements such as "precision", "energy efficiency", "green buildings". back side should list our service offerings

```html
<!DOCTYPE html>
<html lang="en">
<head>
<meta charset="utf-8">
<title>Harborline Facility Systems — Business Card</title>
<link href="https://fonts.googleapis.com/css2?family=Exo+2:wght@700&family=Arimo:wght@400&display=swap" rel="stylesheet">
<style>
  :root {
    --backdrop: #7a6048;
    --card-white: #ffffff;
    --card-black: #000000;
    --green: #5dbb3a;
    --green-deep: #1fa84e;
    --ink: #111111;
    --paper-text: #ffffff;
  }
  * { margin: 0; padding: 0; box-sizing: border-box; }
  html, body { width: 900px; height: 1200px; overflow: hidden; }
  body {
    position: relative;
    background: var(--backdrop);
    font-family: "Arimo", Arial, sans-serif;
  }
  .card {
    position: absolute;
    width: 734px;
    height: 430px;
    border-radius: 26px;
    box-shadow: 0 6px 14px rgba(0, 0, 0, 0.45);
  }
  .card-front { left: 87px; top: 125px; background: var(--card-white); }
  .card-back  { left: 88px; top: 640px; background: var(--card-black); }

  .front-mark {
    position: absolute;
    left: 58px;
    top: 160px;
    width: 200px;
    text-align: center;
    font-family: "Exo 2", sans-serif;
    font-weight: 700;
    font-size: 26px;
    line-height: 1.08;
    letter-spacing: 0.5px;
    color: var(--green-deep);
    text-transform: uppercase;
  }
  .divider {
    position: absolute;
    left: 282px;
    top: 172px;
    width: 2px;
    height: 86px;
    background: var(--green-deep);
  }
  .contact { position: absolute; left: 313px; top: 166px; }
  .person-name {
    font-family: "Exo 2", sans-serif;
    font-weight: 700;
    font-size: 21px;
    letter-spacing: 1px;
    color: var(--ink);
    line-height: 24px;
  }
  .person-title {
    font-family: "Exo 2", sans-serif;
    font-weight: 700;
    font-size: 14px;
    letter-spacing: 0.6px;
    color: var(--green);
    line-height: 18px;
  }
  .contact-line {
    display: flex;
    align-items: center;
    gap: 12px;
    font-size: 16px;
    color: var(--ink);
    height: 24px;
  }
  .contact-line:first-of-type { margin-top: 8px; }
  .contact-line svg { flex: none; }

  .back-mark-shape {
    position: absolute;
    left: 284px;
    top: 72px;
    width: 156px;
    height: 156px;
    border-radius: 50%;
    background: linear-gradient(135deg, var(--green-deep), #a7d93c);
  }
  .back-name {
    position: absolute;
    left: 0;
    right: 0;
    top: 236px;
    text-align: center;
    font-family: "Exo 2", sans-serif;
    font-weight: 700;
    font-size: 28px;
    letter-spacing: 0.5px;
    color: var(--paper-text);
    text-transform: uppercase;
  }
  .services {
    position: absolute;
    left: 0;
    right: 0;
    top: 307px;
    text-align: center;
    font-size: 15.5px;
    line-height: 23px;
    color: var(--paper-text);
    list-style: none;
  }
  .dot { color: var(--green); margin: 0 6px; }
</style>
</head>
<body>
  <section class="card card-front">
    <div class="front-mark">Harborline Facility Systems</div>
    <div class="divider"></div>
    <div class="contact">
      <div class="person-name">DANIEL REYES, P.E., CEM</div>
      <div class="person-title">MANAGING DIRECTOR</div>
      <div class="contact-line">
        <svg width="14" height="18" viewBox="0 0 14 18"><rect x="1" y="1" width="12" height="16" rx="2" fill="none" stroke="#5dbb3a" stroke-width="2"/><rect x="3.5" y="3.5" width="7" height="5" fill="#5dbb3a"/></svg>
        <span>555.204.7731</span>
      </div>
      <div class="contact-line">
        <svg width="16" height="12" viewBox="0 0 16 12"><rect x="0" y="0" width="16" height="12" fill="#5dbb3a"/><path d="M0 0 L8 7 L16 0" fill="none" stroke="#fff" stroke-width="1.5"/></svg>
        <span>daniel.reyes@harborlinefacility.com</span>
      </div>
    </div>
  </section>

  <section class="card card-back">
    <div class="back-mark-shape"></div>
    <div class="back-name">Harborline Facility Systems</div>
    <ul class="services">
      <li>Energy audit<span class="dot">•</span>Building automation systems<span class="dot">•</span>Commissioning and retro-commissioning</li>
      <li>HVAC control optimization<span class="dot">•</span>Corvane AX / 4 System Integrator<span class="dot">•</span>PACE third-party review</li>
      <li>Healthcare, commercial, retail, office buildings</li>
    </ul>
  </section>
</body>
</html>
```